Dental Office Business Card

We need a business card for our pediatric dentistry office.
On one side the design needs to contain the following:
our logo (attached)
Vento Pediatric Grins
Soraya Kadbelani, DDS
Board Certified Pediatric Dentist
Tel: (555) 318-2747)
Fax: (555) 264-8031
Email: info@ventopediatricgrins.example
Web: www.ventopediatricgrins.example
Address: 41 Brindle Ave, Suite 208, Larkhaven, QX 02099

On the other side of the card, the design needs to have an appointment reminder (date and time as well as day of the week) similar to the design attached (no need for appointment reason “For”)

```html
<!DOCTYPE html>
<html lang="en">
<head>
<meta charset="utf-8">
<title>Vento Pediatric Grins – Business Card</title>
<link href="https://fonts.googleapis.com/css2?family=Montserrat:wght@500;700&family=Poppins:ital,wght@0,400;0,500;1,400&display=swap" rel="stylesheet">
<style>
  :root {
    --backdrop: #3b3b3b;
    --card: #ffffff;
    --ink: #1f1f1f;
    --ink-soft: #3a3a3a;
    --green: #9fd3a4;
    --green-line: #8ccb93;
    --green-faint: #eef6ef;
    --rule: #2b2b2b;
  }
  * { box-sizing: border-box; margin: 0; padding: 0; }
  html, body { width: 1200px; height: 694px; overflow: hidden; }
  body {
    background: var(--backdrop);
    font-family: "Poppins", sans-serif;
    color: var(--ink);
    position: relative;
  }
  .card {
    position: absolute;
    top: 187px;
    width: 560px;
    height: 320px;
    background: var(--card);
    border-radius: 22px;
    overflow: hidden;
    box-shadow: 0 14px 30px rgba(0,0,0,.35);
  }
  .card--back { left: 26px; }
  .card--front { left: 614px; }

  /* Back: appointment reminder */
  .faint-mark {
    position: absolute; right: 40px; top: 30px;
    width: 230px; height: 230px; border-radius: 50%;
    background: var(--green-faint);
  }
  .appt-title {
    position: absolute; left: 40px; top: 34px;
    font-family: "Montserrat", sans-serif; font-weight: 700;
    font-size: 26px; letter-spacing: .5px; color: var(--ink-soft);
  }
  .field {
    position: absolute; display: flex; align-items: flex-end;
    font-size: 17px; color: var(--ink-soft);
  }
  .field .rule { flex: 1; border-bottom: 1px solid var(--rule); margin-left: 8px; height: 1px; margin-bottom: 6px; }
  .field--name { left: 40px; top: 96px; width: 480px; }
  .field--date { left: 40px; top: 144px; width: 250px; }
  .field--time { left: 300px; top: 144px; width: 220px; }
  .days {
    position: absolute; left: 40px; top: 206px; width: 480px;
    display: flex; justify-content: space-between; list-style: none;
  }
  .day { display: flex; align-items: center; gap: 6px; font-size: 16px; color: var(--ink-soft); }
  .day .box { width: 17px; height: 17px; border: 2px solid var(--green-line); border-radius: 4px; }
  .appt-note {
    position: absolute; left: 20px; bottom: 34px; width: 520px;
    text-align: center; font-style: italic; font-size: 10.5px;
    white-space: nowrap; color: var(--ink-soft);
  }

  /* Front: practice details */
  .brand {
    position: absolute; left: 30px; top: 34px;
    display: flex; align-items: center; gap: 10px;
  }
  .brand .dot { width: 34px; height: 34px; border-radius: 50%; background: var(--green); }
  .brand .brand-name {
    font-family: "Montserrat", sans-serif; font-weight: 700;
    font-size: 20px; line-height: 1.1; color: var(--ink); width: 160px;
  }
  .practice {
    position: absolute; right: 28px; top: 28px; text-align: right;
  }
  .practice-name { font-family: "Montserrat", sans-serif; font-weight: 700; font-size: 19px; }
  .practice-line { font-size: 12.5px; color: var(--ink-soft); line-height: 1.4; }
  .big-mark {
    position: absolute; right: 36px; top: 118px;
    width: 150px; height: 150px; border-radius: 50%; background: var(--green);
  }
  .swoosh { position: absolute; right: 0; bottom: 0; }
  .address {
    position: absolute; left: 40px; top: 140px;
    font-size: 14px; line-height: 1.45; color: var(--ink);
  }
  .contacts { position: absolute; left: 40px; top: 196px; list-style: none; }
  .contacts li {
    display: flex; align-items: center; gap: 8px;
    font-size: 14px; line-height: 1.55; color: var(--ink);
  }
  .contacts svg { width: 13px; height: 13px; flex: none; }
</style>
</head>
<body>

<section class="card card--back" aria-label="Appointment reminder side">
  <div class="faint-mark"></div>
  <h2 class="appt-title">YOUR NEXT APPOINTMENT</h2>
  <div class="field field--name">Name :<span class="rule"></span></div>
  <div class="field field--date">Date :<span class="rule"></span></div>
  <div class="field field--time">Time :<span class="rule"></span></div>
  <ul class="days">
    <li class="day"><span class="box"></span>Mon</li>
    <li class="day"><span class="box"></span>Tue</li>
    <li class="day"><span class="box"></span>Wed</li>
    <li class="day"><span class="box"></span>Thu</li>
    <li class="day"><span class="box"></span>Fri</li>
    <li class="day"><span class="box"></span>Sat</li>
    <li class="day"><span class="box"></span>Sun</li>
  </ul>
  <p class="appt-note">If you are unable to keep your Appointment, please let us know at least 24 hours in advance</p>
</section>

<section class="card card--front" aria-label="Practice details side">
  <div class="brand">
    <span class="dot"></span>
    <span class="brand-name">Vento Pediatric Grins</span>
  </div>

  <div class="practice">
    <p class="practice-name">Vento Pediatric Grins</p>
    <p class="practice-line">Soraya Kadbelani, DDS</p>
    <p class="practice-line">Board Certified Pediatric Dentist</p>
  </div>

  <div class="big-mark"></div>
  <svg class="swoosh" width="180" height="120" viewBox="0 0 180 120" aria-hidden="true">
    <path d="M20 112 C90 116 150 80 180 30" fill="none" stroke="var(--green)" stroke-width="7" stroke-linecap="round"/>
  </svg>

  <p class="address">41 Brindle Ave, Suite 208<br>Larkhaven, QX 02099</p>

  <ul class="contacts">
    <li>
      <svg viewBox="0 0 16 16" aria-hidden="true"><path d="M3 1h3l1.5 4-2 1.2a9 9 0 0 0 4.3 4.3L11 8.5l4 1.5v3c0 1-1 2-2 2C6.5 15 1 9.5 1 3c0-1 1-2 2-2z" fill="var(--green-line)"/></svg>
      (555) 318-2747
    </li>
    <li>
      <svg viewBox="0 0 16 16" aria-hidden="true"><rect x="4" y="1" width="8" height="5" fill="var(--green-line)"/><rect x="1" y="6" width="14" height="6" rx="1" fill="var(--green-line)"/><rect x="4" y="10" width="8" height="5" fill="#fff" stroke="var(--green-line)" stroke-width="1.5"/></svg>
      (555) 264-8031
    </li>
    <li>
      <svg viewBox="0 0 16 16" aria-hidden="true"><rect x="1" y="3" width="14" height="10" rx="1" fill="var(--green-line)"/><path d="M1.5 3.5 8 9l6.5-5.5" fill="none" stroke="#fff" stroke-width="1.4"/></svg>
      info@ventopediatricgrins.example
    </li>
    <li>
      <svg viewBox="0 0 16 16" aria-hidden="true"><circle cx="8" cy="8" r="7" fill="var(--green-line)"/><path d="M1 8h14M8 1c-3 3.5-3 10.5 0 14M8 1c3 3.5 3 10.5 0 14" fill="none" stroke="#fff" stroke-width="1"/></svg>
      www.ventopediatricgrins.example
    </li>
  </ul>
</section>

</body>
</html>
```